Web form face-lift for an online startup

We are a web startup building a SaaS application for the freight industry. The project is mainly dedicated to the paint the main form that our customer are using along the search results that the they get. All details are in the attached documents.
Updates
The application serves the Freight Forwarders community so please think towards this industry when using background images, banners, colors, icons, etc. Computer and technology images are irrelevant.
Customer fields at the top of the page is actually part of the form.
Target Market(s)
Usually business users (Sales people, procurement, shippers, freight forwarders). Some are less tech savvy and some appreciate the new trendy web apps.
Industry/Entity Type
Building
Colors
Designer to choose colors to be used in the design.
Look and feel
Each slider illustrates characteristics of the customer's brand and the style your logo design should communicate.

```html
<!DOCTYPE html>
<html lang="en">
<head>
<meta charset="utf-8">
<title>SaaS Application – Search for Quotes</title>
<link href="https://fonts.googleapis.com/css2?family=Open+Sans:wght@400;600;700&display=swap" rel="stylesheet">
<style>
:root{
  --red:#d13438;
  --teal:#0bb3b5;
  --dark:#545454;
  --ink:#333;
  --line:#c9c9c9;
  --field:#cfcfcf;
  --page:#f5f5f4;
  --white:#fff;
  --link:#2a8fc4;
}
*{box-sizing:border-box;margin:0;padding:0}
html,body{width:1189px;height:1200px;overflow:hidden;background:var(--page);font-family:'Open Sans',Arial,sans-serif;color:var(--ink)}
.stage{position:absolute;left:0;top:0;width:1000px;height:1009px;transform:scale(1.189);transform-origin:0 0}
.abs{position:absolute}
.topbar{left:0;top:0;width:1000px;height:31px;background:var(--red);color:var(--white);font-size:12px}
.topbar span{position:absolute;top:9px}
.caret{display:inline-block;width:0;height:0;border-left:3.5px solid transparent;border-right:3.5px solid transparent;border-top:4px solid currentColor;margin-left:6px;vertical-align:2px}
.header{left:0;top:31px;width:1000px;height:75px;background:var(--teal);border-bottom:2px solid var(--white);box-shadow:0 2px 0 var(--teal)}
.brand{left:16px;top:24px;color:var(--white);font-size:23px;font-weight:400;letter-spacing:.2px}
.menu{top:29px;font-size:13px;color:var(--white);font-weight:600}
.menu.active{background:var(--dark);padding:2px 5px;border-radius:3px;top:27px}
.menu.active::after{content:"";position:absolute;left:70px;bottom:-5px;border-left:5px solid transparent;border-right:5px solid transparent;border-top:5px solid var(--dark)}
.title{left:50px;top:136px;font-size:17px;font-weight:700;display:flex;align-items:center;gap:6px}
.label{font-size:13px;font-weight:600}
.input{background:var(--white);border:1px solid var(--field);font-size:13px;font-weight:600;display:flex;align-items:center;padding-left:9px;height:29px}
.input.center{justify-content:center;padding:0}
.select::after{content:"";position:absolute;right:10px;top:13px;border-left:3.5px solid transparent;border-right:3.5px solid transparent;border-top:4px solid #222}
.check{width:11px;height:11px;border:1px solid #bbb;background:#f2f2f2;border-radius:2px}
.tab{top:259px;height:57px;display:flex;align-items:center;gap:10px;padding-left:8px;color:var(--white);font-weight:700;font-size:13.5px}
.tab .pic{width:50px;height:44px;border-radius:3px}
.card{left:29px;top:316px;width:937px;height:576px;background:var(--white);border:1px solid #bdbdbd;border-radius:4px}
.rule{height:1px;background:var(--line);left:51px;width:885px}
.btn{background:var(--red);color:var(--white);border-radius:3px;font-weight:700;display:flex;align-items:center;justify-content:center}
.radio{width:15px;height:15px;border-radius:50%;border:1px solid #aaa;background:linear-gradient(#fff,#ddd)}
.redlink{color:var(--red);font-weight:700}
.footer{left:0;top:939px;width:1000px;height:70px;background:var(--teal);border-top:4px solid var(--red);box-shadow:inset 0 2px 0 var(--white)}
.footer .links{position:absolute;top:25px;color:var(--white);font-size:13px;font-weight:600;word-spacing:2px}
</style>
</head>
<body>
<div class="stage">
  <div class="abs topbar">
    <span style="left:777px">USD<i class="caret"></i></span>
    <span style="left:842px">English<i class="caret"></i></span>
    <span style="left:915px">Username</span>
  </div>
  <div class="abs header">
    <div class="abs brand">SAAS APPLICATION</div>
    <div class="abs menu active" style="left:248px">Menu Item 1</div>
    <div class="abs menu" style="left:346px">Menu Item 2</div>
    <div class="abs menu" style="left:439px">Menu Item 3</div>
    <div class="abs menu" style="left:531px">Menu Item 4</div>
    <div class="abs menu" style="left:624px">Menu Item 5</div>
    <div class="abs menu" style="left:717px">Menu Item 6</div>
    <div class="abs menu" style="left:809px">Menu Item 7</div>
    <div class="abs menu" style="left:902px">Menu Item 8</div>
  </div>

  <div class="abs title">
    <svg width="22" height="20" viewBox="0 0 22 20"><circle cx="7" cy="7" r="5" fill="none" stroke="#333" stroke-width="2.5"/><line x1="11" y1="11" x2="20" y2="18" stroke="#333" stroke-width="4" stroke-linecap="round"/></svg>
    SEARCH FOR QUOTES
  </div>
  <div class="abs label" style="left:49px;top:178px">Customer</div>
  <div class="abs input" style="left:133px;top:172px;width:271px"></div>
  <div class="abs check" style="left:135px;top:211px"></div>
  <div class="abs" style="left:153px;top:208px;font-size:11px;font-weight:700">Rate Quote ?</div>

  <div class="abs tab" style="left:43px;width:166px;background:var(--teal)">
    <div class="pic" role="img" aria-label="Cardboard box illustration" style="background:linear-gradient(#e3a65a,#b8742f)"></div>BOX / PALLET
  </div>
  <div class="abs tab" style="left:214px;width:240px;background:var(--dark)">
    <div class="pic" role="img" aria-label="Stacked red shipping containers on a pallet" style="background:linear-gradient(#e04a3f,#a3302a)"></div>SHIPPING CONTAINER
  </div>
  <div class="abs tab" style="left:459px;width:170px;background:var(--dark)">
    <div class="pic" role="img" aria-label="Small parcel box illustration" style="width:44px;background:linear-gradient(#c98a4f,#8d5a2e)"></div>SMALL PARCEL
  </div>
  <div class="abs redlink" style="left:651px;top:279px;font-size:14px">more &gt;&gt;</div>

  <div class="abs card"></div>

  <div class="abs label" style="left:66px;top:342px">Qty</div>
  <div class="abs label" style="left:122px;top:342px">Stacklabel</div>
  <div class="abs label" style="left:211px;top:342px">Load</div>
  <div class="abs label" style="left:507px;top:342px">Length</div>
  <div class="abs label" style="left:591px;top:342px">Width</div>
  <div class="abs label" style="left:674px;top:342px">Height</div>
  <div class="abs label" style="left:812px;top:342px">Weight</div>

  <div class="abs input center" style="left:53px;top:368px;width:49px">5</div>
  <div class="abs check" style="left:147px;top:377px"></div>
  <div class="abs input select" style="left:211px;top:368px;width:271px">Box/ Pallet</div>
  <div class="abs input center" style="left:492px;top:368px;width:74px">100</div>
  <div class="abs input center" style="left:576px;top:368px;width:74px">100</div>
  <div class="abs input center" style="left:659px;top:368px;width:74px">100</div>
  <div class="abs input select" style="left:740px;top:368px;width:49px">cm</div>
  <div class="abs input center" style="left:797px;top:368px;width:74px">100</div>
  <div class="abs input select" style="left:879px;top:368px;width:49px">kg</div>

  <div class="abs btn" style="left:65px;top:429px;width:142px;height:31px;font-size:12px;gap:8px">
    <svg width="11" height="11" viewBox="0 0 11 11"><path d="M5.5 0v11M0 5.5h11" stroke="#fff" stroke-width="2.6"/></svg>Add More Units
  </div>

  <div class="abs rule" style="top:479px"></div>
  <div class="abs label" style="left:516px;top:505px">Total</div>
  <div class="abs input center" style="left:562px;top:498px;width:74px">5</div>
  <div class="abs input center" style="left:642px;top:498px;width:74px">1</div>
  <div class="abs input select" style="left:715px;top:498px;width:74px">CBM</div>
  <div class="abs input center" style="left:797px;top:498px;width:74px">100</div>
  <div class="abs input select" style="left:879px;top:498px;width:49px">kg</div>
  <div class="abs rule" style="top:549px"></div>

  <div class="abs label" style="left:57px;top:580px">From</div>
  <div class="abs input" style="left:110px;top:575px;width:271px">Shipping address or port</div>
  <div class="abs label" style="left:629px;top:580px">To</div>
  <div class="abs input" style="left:663px;top:575px;width:271px">Shipping address or port</div>

  <div class="abs" style="left:56px;top:647px;font-size:17px;font-weight:700">OPTIONS</div>
  <div class="abs radio" style="left:67px;top:684px"></div>
  <div class="abs label" style="left:90px;top:683px">Import</div>
  <div class="abs radio" style="left:149px;top:684px"></div>
  <div class="abs label" style="left:172px;top:683px">Export</div>
  <div class="abs label" style="left:263px;top:683px">Incotem: <span style="color:var(--link)">FCA</span></div>

  <div class="abs check" style="left:394px;top:685px"></div>
  <svg class="abs" style="left:410px;top:680px" width="21" height="21" viewBox="0 0 21 21"><circle cx="10.5" cy="10.5" r="8.5" fill="#fff" stroke="#d13438" stroke-width="2"/><rect x="6" y="7" width="9" height="7" fill="#2a6fb8"/><line x1="4.5" y1="16.5" x2="16.5" y2="4.5" stroke="#d13438" stroke-width="2"/></svg>
  <div class="abs check" style="left:447px;top:685px"></div>
  <svg class="abs" style="left:463px;top:680px" width="21" height="21" viewBox="0 0 21 21"><circle cx="10.5" cy="10.5" r="8.5" fill="#fff" stroke="#d13438" stroke-width="2"/><circle cx="10.5" cy="10.5" r="4.5" fill="#2a6fb8"/><line x1="4.5" y1="16.5" x2="16.5" y2="4.5" stroke="#d13438" stroke-width="2"/></svg>
  <div class="abs check" style="left:499px;top:685px"></div>
  <svg class="abs" style="left:516px;top:680px" width="21" height="21" viewBox="0 0 21 21"><circle cx="10.5" cy="10.5" r="8.5" fill="#fff" stroke="#d13438" stroke-width="2"/><path d="M7 8h7M7 13h7" stroke="#2a6fb8" stroke-width="2"/><line x1="4.5" y1="16.5" x2="16.5" y2="4.5" stroke="#d13438" stroke-width="2"/></svg>

  <div class="abs input select" style="left:663px;top:678px;width:271px">Price Level</div>
  <div class="abs redlink" style="left:845px;top:738px;font-size:13px">More Options</div>

  <div class="abs btn" style="left:396px;top:798px;width:201px;height:38px;font-size:16px;font-weight:600">SEARCH QUOTES</div>
  <div class="abs label" style="left:637px;top:808px">or</div>
  <div class="abs redlink" style="left:666px;top:806px;font-size:15.5px">Create manually</div>

  <div class="abs footer">
    <div class="links" style="left:49px">About Us &nbsp;|&nbsp; Privacy Policy &nbsp;|&nbsp; Terms Of Service &nbsp;|&nbsp; News</div>
    <div class="links" style="left:758px">Blog &nbsp;|&nbsp; Friendnet &nbsp;|&nbsp; Chirper</div>
  </div>
</div>
</body>
</html>
```